Logo-Design für Internetvertrieb von Tierbedarf
Zielgruppe
Internetvertrieb von Tierbedarf
Zielgruppe: Tierhalter jeglicher Altersstufe, die Ihr (Haus-)Tier lieben
Aufgabenstellung
seriöses Design, das aber trotzdem vermittelt, was man mit seinem Tier verbindet....
Liebe, Freund, Freizeit, Entspannung, Spass etc.

```html
<!DOCTYPE html>
<html lang="de">
<head>
<meta charset="utf-8">
<title>Felma Tierhaus – Visitenkarten</title>
<link href="https://fonts.googleapis.com/css2?family=Montserrat:wght@400;500&display=swap" rel="stylesheet">
<style>
  :root {
    --stage: #c2c1bf;
    --card: #ffffff;
    --crimson: #c81e47;
    --ink: #555556;
    --shadow: rgba(40, 40, 40, 0.45);
  }
  html, body {
    margin: 0;
    padding: 0;
    width: 1200px;
    height: 1176px;
    overflow: hidden;
    background: var(--stage);
    font-family: "Montserrat", Arial, sans-serif;
    color: var(--ink);
  }
  .card {
    position: absolute;
    left: 259px;
    width: 724px;
    height: 458px;
    background: var(--card);
    box-shadow: 6px 8px 10px var(--shadow);
  }
  .card--front { top: 87px; }
  .card--back { top: 641px; }

  .brand {
    position: absolute;
    display: flex;
    align-items: center;
    color: var(--ink);
    font-weight: 500;
    white-space: nowrap;
    line-height: 1;
  }
  .brand__dot {
    border-radius: 50%;
    background: var(--crimson);
    flex: none;
  }
  .card--front .brand { left: 16px; top: 22px; gap: 14px; font-size: 34px; }
  .card--front .brand__dot { width: 110px; height: 110px; }
  .card--back .brand { left: 96px; top: 154px; gap: 22px; font-size: 50px; }
  .card--back .brand__dot { width: 150px; height: 150px; }

  .person__name {
    position: absolute;
    left: 380px;
    top: 160px;
    margin: 0;
    font-size: 44px;
    font-weight: 400;
    letter-spacing: 1px;
    color: var(--crimson);
    line-height: 1;
  }
  .person__role {
    position: absolute;
    left: 438px;
    top: 212px;
    margin: 0;
    font-size: 18px;
    letter-spacing: 0.5px;
    line-height: 1;
  }

  .address {
    position: absolute;
    left: 35px;
    top: 300px;
    display: flex;
    gap: 12px;
    font-size: 18px;
    line-height: 23px;
    font-style: normal;
    letter-spacing: 0.3px;
  }
  .address svg { margin-top: 2px; flex: none; }

  .contact {
    position: absolute;
    left: 382px;
    top: 300px;
    margin: 0;
    padding: 0;
    list-style: none;
    font-size: 18px;
    letter-spacing: 0.3px;
  }
  .contact li {
    display: flex;
    align-items: center;
    gap: 10px;
    height: 24px;
    margin-bottom: 14.5px;
  }
  .contact svg { flex: none; }

  .accent-bar {
    position: absolute;
    left: 382px;
    bottom: 0;
    width: 342px;
    height: 19px;
    background: var(--crimson);
  }
</style>
</head>
<body>
  <section class="card card--front">
    <div class="brand"><span class="brand__dot"></span>Felma Tierhaus</div>

    <h1 class="person__name">YOUR NAME</h1>
    <p class="person__role">JOB POSITION</p>

    <address class="address">
      <svg width="20" height="26" viewBox="0 0 20 26" aria-hidden="true">
        <path d="M10 1C5 1 1.5 4.6 1.5 9.3 1.5 15 10 25 10 25s8.5-10 8.5-15.7C18.5 4.6 15 1 10 1z" fill="var(--crimson)"/>
        <circle cx="10" cy="9.3" r="3.3" fill="#fff"/>
      </svg>
      <span>Your City Adress<br>Street LocationXXXX,<br>Germany</span>
    </address>

    <ul class="contact">
      <li>
        <svg width="22" height="22" viewBox="0 0 22 22" aria-hidden="true">
          <circle cx="11" cy="11" r="10" fill="none" stroke="var(--crimson)" stroke-width="1.6"/>
          <path d="M7.5 6c.8-.5 1.4-.3 1.8.4l.9 1.6c.3.6.1 1.1-.4 1.5l-.6.4c.5 1.4 1.5 2.5 2.9 3l.4-.6c.4-.5.9-.7 1.5-.4l1.6.9c.7.4.8 1 .4 1.8-.6 1-1.7 1.5-2.9 1.1C9.9 14.8 7.2 12.1 6.3 9c-.3-1.2.2-2.3 1.2-3z" fill="var(--crimson)"/>
        </svg>
        +00 000 000 00 000
      </li>
      <li>
        <svg width="24" height="18" viewBox="0 0 24 18" aria-hidden="true">
          <rect x="1" y="2" width="22" height="14" fill="var(--crimson)"/>
          <path d="M1 2l11 8 11-8" fill="none" stroke="#fff" stroke-width="1.4"/>
        </svg>
        info@felmatierhaus.de
      </li>
      <li>
        <svg width="24" height="24" viewBox="0 0 24 24" aria-hidden="true">
          <g fill="none" stroke="var(--crimson)" stroke-width="1.5">
            <circle cx="12" cy="12" r="10"/>
            <ellipse cx="12" cy="12" rx="4.5" ry="10"/>
            <line x1="2" y1="12" x2="22" y2="12"/>
            <path d="M4 6.5h16M4 17.5h16"/>
          </g>
        </svg>
        www.felmatierhaus.de
      </li>
    </ul>

    <div class="accent-bar"></div>
  </section>

  <section class="card card--back">
    <div class="brand"><span class="brand__dot"></span>Felma Tierhaus</div>
  </section>
</body>
</html>
```